Premium Gold Vodka Label Design

English ------------------- We need a label for a Vodka Bottle. Its a sparkling premium vodka with gold inside. The design should look premium. We tried it on our selves but it looks horrible. Therefore we need your help. The current name is lumora K, but we are open for any better suggestion. We attached the selfmade design. The label will be printed on the bottle. We have other design jobs for you (logo, other sorts)! English ------------------------ We need a label for a vodka bottle. This is a premium vodka which is offset with gold. The design should look like this. We have tried so far and failed. That is why we need your support. The name is so far lumora K. If you have better suggestions we would be pleased about other suggestions / ideas. In the appendix the failed design is stored. The label is to be applied by screen printing. In the case of good work follow-up projects are guaranteed (logo, other varieties, etc)!
Updates

Project Deadline Extended
Reason: We need more time for the decision.

Target Market(s)

USA

Colors

Designer to choose colors to be used in the design.

Requirements
Must have
• English ------------------------ The needed text is on our selfmade label that is attached. English ------------------------ The required texts are stored in the attached design.
Nice to have
• English ------------------------ Transparent places are allowed because we want to print the label on the bottom. English ------------------------ As the label is applied by screen printing, transparent areas are also possible.

```html
<!DOCTYPE html>
<html lang="en">
<head>
<meta charset="utf-8">
<title>AURELO Premium Gold Vodka – Label Set</title>
<link rel="stylesheet" href="https://fonts.googleapis.com/css2?family=Jost:wght@500;600;700&family=Pinyon+Script&display=swap">
<style>
  :root {
    --backdrop: #42403c;
    --paper: #ecebe3;
    --ink-dark: #2b2722;
    --ink-band: #4a4334;
    --gold-light: #cbbd9a;
    --gold-mid: #a8976f;
    --gold-dark: #76684a;
    --gold-text-top: #8a7650;
    --gold-text-bottom: #4e3f25;
    --badge-dark: #2f2e2b;
    --batch-red: #d8432f;
  }
  * { margin: 0; padding: 0; box-sizing: border-box; }
  html, body { width: 1200px; height: 1200px; overflow: hidden; background: var(--backdrop); }
  .canvas { position: relative; width: 1200px; height: 1200px; font-family: "Jost", sans-serif; }

  /* Neck badge */
  .neck-badge {
    position: absolute; left: 513px; top: 95px; width: 158px; height: 158px;
    transform: rotate(45deg);
    background: radial-gradient(circle at 50% 50%, #5a5240 0%, #3a3630 45%, var(--badge-dark) 75%);
    box-shadow: 0 3px 8px rgba(0,0,0,0.35);
  }

  /* Seal band */
  .seal-band { position: absolute; left: 220px; top: 333px; width: 760px; height: 58px; background: var(--paper); }
  .seal-tab {
    position: absolute; left: 534px; top: 322px; width: 132px; height: 80px;
    background: var(--paper); border-radius: 14px;
  }
  .band-line { position: absolute; height: 1.5px; background: linear-gradient(90deg, var(--gold-dark), var(--gold-light), var(--gold-dark)); }
  .band-motto {
    position: absolute; top: 352px; width: 210px; text-align: center;
    font-weight: 700; font-size: 15px; letter-spacing: 3.2px; color: var(--ink-band); line-height: 20px;
  }
  .band-motto.left { left: 286px; }
  .band-motto.right { left: 706px; transform: rotate(180deg); }

  .tab-label {
    position: absolute; font-weight: 700; font-size: 7px; letter-spacing: 0.8px; color: var(--ink-dark);
    transform: rotate(-90deg); transform-origin: center; white-space: nowrap; width: 60px; text-align: center;
  }
  .tab-number {
    position: absolute; font-family: "Pinyon Script", cursive; font-size: 28px; color: var(--batch-red);
    transform: rotate(-70deg); transform-origin: center; white-space: nowrap; width: 50px; text-align: center; line-height: 30px;
  }

  /* Front label */
  .front-label {
    position: absolute; left: 406px; top: 422px; width: 374px; height: 448px;
    background: linear-gradient(100deg, #e4e3da 0%, var(--paper) 18%, var(--paper) 100%);
    clip-path: polygon(0 0, 100% 0, 97.9% 100%, 2.4% 100%);
  }
  .brand-name {
    position: absolute; left: 592px; top: 644px;
    transform: translate(-50%, -50%) rotate(-90deg);
    font-weight: 700; font-size: 40px; letter-spacing: 16px; white-space: nowrap;
    background: linear-gradient(90deg, var(--gold-text-bottom), var(--gold-text-top));
    -webkit-background-clip: text; background-clip: text; color: transparent;
  }

  /* Gold back label */
  .gold-label {
    position: absolute; left: 474px; top: 926px; width: 238px; height: 172px;
    background: linear-gradient(80deg, var(--gold-light) 0%, var(--gold-mid) 35%, #8f7f5c 70%, var(--gold-dark) 100%);
    box-shadow: 0 2px 6px rgba(0,0,0,0.3);
    text-align: center; color: var(--ink-dark);
  }
  .gold-label .kt { position: absolute; top: 28px; width: 100%; font-weight: 700; font-size: 24px; letter-spacing: 1px; line-height: 26px; }
  .gold-label .script { position: absolute; top: 46px; width: 100%; font-family: "Pinyon Script", cursive; font-size: 28px; line-height: 30px; }
  .gold-label .product { position: absolute; top: 78px; width: 100%; font-weight: 700; font-size: 24px; letter-spacing: 2px; line-height: 26px; }
  .gold-label .detail { position: absolute; width: 100%; font-weight: 600; font-size: 9.5px; letter-spacing: 1.6px; line-height: 12px; }
  .gold-label .detail .amp { font-family: "Pinyon Script", cursive; font-size: 14px; letter-spacing: 0; }
</style>
</head>
<body>
<main class="canvas">

  <div class="neck-badge" role="img" aria-label="Neck badge with engraved gold emblem: hand holding a gold bar, reading Premium Gold, 24 KT, Handcrafted"></div>

  <div class="seal-band"></div>
  <div class="seal-tab"></div>

  <div class="band-line" style="left:236px; top:346px; width:260px;"></div>
  <div class="band-line" style="left:236px; top:377px; width:260px;"></div>
  <div class="band-line" style="left:706px; top:346px; width:260px;"></div>
  <div class="band-line" style="left:706px; top:377px; width:260px;"></div>

  <p class="band-motto left">BEWARE THE TOUCH</p>
  <p class="band-motto right">BEWARE THE TOUCH</p>

  <span class="tab-number" style="left:545px; top:347px;">34</span>
  <span class="tab-label" style="left:560px; top:358px;">BATCH NO</span>
  <span class="tab-number" style="left:589px; top:347px;">126</span>
  <span class="tab-label" style="left:607px; top:358px;">BOTTLE NO</span>

  <section class="front-label"></section>
  <h1 class="brand-name">AURELO</h1>

  <section class="gold-label">
    <p class="kt">24KT</p>
    <p class="script">Premium Gold</p>
    <p class="product">VODKA</p>
    <p class="detail" style="top:106px;">DISTILLED <span class="amp">8</span> FILTERED</p>
    <p class="detail" style="top:121px;">MADE IN GERMANY</p>
    <p class="detail" style="top:135px; letter-spacing:1.3px;">40%ALC VOL 200ML 80PROOF</p>
  </section>

</main>
</body>
</html>
```